Business Card / Flyer Design Project

Prevent Accidents in your HomeSafety grab barsChild safety and child proofingEarthquake proofingOur company provide a service to help prevent home accidents of all types, from bathroom slip and fall accidents to baby proofing and earthquake safety. Maybe a 4x6 flyer type would be the best for handouts? Maybe a graphic of some kind? Company name, Dwelling Guard Crew. Contractors license # 736215

Thad Friday818-419-4212

```html
<!DOCTYPE html>
<html lang="en">
<head>
<meta charset="utf-8">
<title>Dwelling Guard Crew – Business Card</title>
<link rel="stylesheet" href="https://fonts.googleapis.com/css2?family=Montserrat:wght@500;600;700;800&display=swap">
<style>
  :root {
    --backdrop: #e6e3df;
    --ink-black: #0d0d0d;
    --card-dark: #1a1a1a;
    --card-glow: #3a3a3a;
    --brand-orange: #f08a1c;
    --paper-white: #ffffff;
    --text-white: #f2f2f2;
  }
  * { margin: 0; padding: 0; box-sizing: border-box; }
  html, body {
    width: 1200px; height: 784px; overflow: hidden;
    background: var(--backdrop);
    font-family: "Montserrat", sans-serif;
  }
  .canvas {
    position: relative; width: 1200px; height: 784px;
    display: flex; align-items: center; justify-content: center; gap: 40px;
  }
  .card {
    position: relative; width: 540px; height: 309px; overflow: hidden;
    box-shadow: 0 6px 18px rgba(0,0,0,0.18);
  }

  /* Back side */
  .card-back {
    background: radial-gradient(ellipse at 40% 40%, var(--card-glow) 0%, var(--card-dark) 55%, var(--ink-black) 100%);
  }
  .service-list {
    position: absolute; left: 0; width: 380px; top: 58px;
    list-style: none; text-align: center;
  }
  .service-list li {
    font-size: 13px; font-weight: 600; letter-spacing: 3px;
    text-transform: uppercase; line-height: 1; margin-bottom: 24px;
  }
  .service-list .accent { color: var(--brand-orange); }
  .service-list .plain { color: var(--text-white); }
  .back-brand {
    position: absolute; right: 22px; bottom: 92px;
    display: flex; flex-direction: column; align-items: center; gap: 6px;
  }
  .back-brand .brand-dot {
    width: 34px; height: 34px; border-radius: 50%;
    background: var(--brand-orange);
  }
  .back-brand .brand-name {
    color: var(--brand-orange); font-size: 11px; font-weight: 700; white-space: nowrap;
  }

  /* Front side */
  .card-front { background: var(--ink-black); }
  .card-front svg.front-shapes { position: absolute; inset: 0; }
  .front-brand {
    position: absolute; left: 0; right: 0; top: 34px;
    display: flex; flex-direction: column; align-items: center; gap: 12px;
  }
  .front-brand .brand-dot {
    width: 82px; height: 82px; border-radius: 50%;
    background: var(--brand-orange);
  }
  .front-brand .brand-name {
    color: var(--brand-orange); font-size: 26px; font-weight: 800; letter-spacing: 0.2px;
  }
  .contact {
    position: absolute; left: 0; right: 0; top: 214px; text-align: center;
  }
  .contact .person {
    color: var(--brand-orange); font-size: 19px; font-weight: 600; text-transform: uppercase;
  }
  .contact .phone {
    color: var(--text-white); font-size: 24px; font-weight: 600; margin-top: 4px;
  }
</style>
</head>
<body>
  <main class="canvas">
    <section class="card card-back" aria-label="Card back">
      <ul class="service-list">
        <li class="accent">Prevent accidents in your home</li>
        <li class="plain">Safety grab bars</li>
        <li class="accent">Child safety and child proofing</li>
        <li class="plain">Earthquake proofing</li>
      </ul>
      <div class="back-brand">
        <span class="brand-dot"></span>
        <span class="brand-name">Dwelling Guard Crew</span>
      </div>
    </section>

    <section class="card card-front" aria-label="Card front">
      <svg class="front-shapes" viewBox="0 0 540 309" width="540" height="309" aria-hidden="true">
        <path d="M0,0 H540 V50 C440,210 180,222 0,172 Z" fill="var(--paper-white)"/>
        <path d="M0,172 C180,222 440,210 540,50 V92 C440,236 180,234 0,184 Z" fill="var(--brand-orange)"/>
      </svg>
      <div class="front-brand">
        <span class="brand-dot"></span>
        <span class="brand-name">Dwelling Guard Crew</span>
      </div>
      <div class="contact">
        <p class="person">Lorn Beckett</p>
        <p class="phone">555-307-6981</p>
      </div>
    </section>
  </main>
</body>
</html>
```